Tri-fold Brochure for Law Firm

Double-sided brochure to be folded into 6 sides tri-fold brochure for an estate planning special for new parents or parents-to-be. Brochure will be placed in classes for new parents/young parents.

Target Market(s)

New Parents Aged 24-34

Industry/Entity Type

Law Firm

Font styles to use
Serif

Requirements
Must have
• The information provided in the word document.
Nice to have
• Highlight the phrase "for New Parents."
• You may use the color scheme from our website:
• http://k27.9qd.sitehostbox.net/

```html
<!DOCTYPE html>
<html lang="en">
<head>
<meta charset="utf-8">
<title>Hartwell Legal — Estate Planning Special for New Parents</title>
<link rel="stylesheet" href="https://fonts.googleapis.com/css2?family=Arimo:wght@400;700&family=Oswald:wght@300;400&family=Roboto+Condensed:wght@500;700&family=Tinos&display=swap">
<style>
  :root {
    --page-bg: #ececec;
    --gold: #f6b208;
    --gold-deep: #f09e00;
    --charcoal: #2c2c2c;
    --slate: #3a3a3c;
    --ink: #222;
    --paper: #f4f4f4;
    --white: #fff;
  }
  * { margin: 0; padding: 0; box-sizing: border-box; }
  html, body { width: 1200px; height: 1200px; overflow: hidden; }
  body { background: var(--page-bg); font-family: "Arimo", Arial, sans-serif; }

  .spread { position: absolute; left: 30px; top: 247px; width: 1140px; height: 705px; }
  .spread-art { position: absolute; inset: 0; width: 1140px; height: 705px; display: block; }

  /* inside panel text */
  .why-text {
    position: absolute; left: 36px; top: 425px; width: 312px;
    color: var(--white); font-size: 9.4px; line-height: 1.32; text-align: justify;
  }
  .why-text h3 { font-size: 11.5px; font-weight: 700; margin-bottom: 3px; }
  .why-text p { margin-bottom: 6px; }
  .why-text h3 + p { margin-top: 0; }
  .why-text p + h3 { margin-top: 8px; }

  .offer { position: absolute; left: 425px; top: 70px; display: flex; gap: 18px; color: var(--white); }
  .offer-price { text-align: center; }
  .offer-price .amount { font-family: "Oswald", sans-serif; font-weight: 400; font-size: 64px; line-height: 1; color: var(--gold); }
  .offer-price .per { font-family: "Oswald", sans-serif; font-weight: 300; font-size: 25px; line-height: 1.3; }
  .offer-terms { font-family: "Oswald", sans-serif; font-weight: 300; font-size: 16px; line-height: 1.65; text-transform: uppercase; padding-top: 16px; }

  .contact { position: absolute; left: 380px; width: 380px; top: 546px; text-align: center; color: var(--ink); }
  .contact h2 {
    display: inline-block; font-family: "Arimo", sans-serif; font-weight: 400; font-size: 27px;
    letter-spacing: 0.5px; border-bottom: 2px solid var(--ink); line-height: 1.05; margin-bottom: 9px;
  }
  .contact p { font-size: 13.5px; line-height: 1.3; }

  .brand { position: absolute; left: 822px; top: 48px; display: flex; align-items: center; gap: 20px; }
  .brand-dot { width: 40px; height: 40px; border-radius: 50%; background: var(--gold); }
  .brand-name { font-family: "Tinos", serif; font-size: 32px; line-height: 1.08; color: var(--slate); letter-spacing: 1px; }

  .cover-headline { position: absolute; left: 760px; width: 380px; top: 583px; text-align: center; font-family: "Roboto Condensed", sans-serif; font-weight: 700; text-transform: uppercase; }
  .cover-headline .lead { display: block; font-size: 27px; color: var(--charcoal); line-height: 1.1; }
  .cover-headline .accent { display: block; font-size: 37px; color: var(--white); line-height: 1.15; letter-spacing: 0.5px; }
</style>
</head>
<body>
<main class="spread">
  <svg class="spread-art" viewBox="0 0 1140 705" xmlns="http://www.w3.org/2000/svg">
    <defs>
      <linearGradient id="gold-fill" x1="0" y1="0" x2="0" y2="1">
        <stop offset="0" stop-color="#f8c21e"/><stop offset="1" stop-color="#f09e00"/>
      </linearGradient>
      <linearGradient id="paper-fill" x1="0" y1="0" x2="1" y2="1">
        <stop offset="0" stop-color="#ffffff"/><stop offset="1" stop-color="#dcdcdc"/>
      </linearGradient>
      <linearGradient id="dark-fill" x1="0" y1="0" x2="1" y2="1">
        <stop offset="0" stop-color="#3c3c3e"/><stop offset="1" stop-color="#1f1f21"/>
      </linearGradient>
      <linearGradient id="suit-photo" x1="0" y1="0" x2="1" y2="1">
        <stop offset="0" stop-color="#1c2026"/><stop offset="0.55" stop-color="#5d6873"/><stop offset="1" stop-color="#c9d6df"/>
      </linearGradient>
      <radialGradient id="scales-photo" cx="0.5" cy="0.4" r="0.7">
        <stop offset="0" stop-color="#e9d7c4"/><stop offset="0.5" stop-color="#7a5d7e"/><stop offset="1" stop-color="#3a2c2a"/>
      </radialGradient>
      <radialGradient id="laptop-photo" cx="0.5" cy="0.5" r="0.6">
        <stop offset="0" stop-color="#cfe6f3"/><stop offset="1" stop-color="#f3f6f8"/>
      </radialGradient>
      <linearGradient id="team-photo" x1="0" y1="0" x2="1" y2="1">
        <stop offset="0" stop-color="#ece8e2"/><stop offset="0.5" stop-color="#3b3c42"/><stop offset="1" stop-color="#b8b4ad"/>
      </linearGradient>
    </defs>

    <!-- Panel 1: why every parent needs a will -->
    <g class="panel-why">
      <rect x="0" y="0" width="380" height="705" fill="url(#gold-fill)"/>
      <g role="img" aria-label="Businessman in a dark suit pointing at floating portrait tiles">
        <path d="M0 0H380V355C260 362 120 335 0 290Z" fill="url(#suit-photo)"/>
      </g>
      <path d="M0 290C120 335 260 362 380 355V395C250 405 110 382 0 332Z" fill="#ffffff"/>
      <path d="M0 332C110 382 250 405 380 395" fill="none" stroke="var(--charcoal)" stroke-width="5"/>
      <rect x="0" y="687" width="380" height="18" fill="var(--charcoal)"/>
    </g>

    <!-- Panel 2: offer and contact -->
    <g class="panel-offer">
      <rect x="380" y="0" width="380" height="705" fill="url(#paper-fill)"/>
      <path d="M380 0H760V225C700 250 640 280 560 300L380 320Z" fill="url(#dark-fill)"/>
      <path d="M620 300C680 270 720 250 760 232" fill="none" stroke="var(--gold)" stroke-width="5"/>
      <circle cx="561" cy="360" r="132" fill="#ffffff"/>
      <circle cx="561" cy="360" r="121" fill="none" stroke="var(--gold)" stroke-width="6"/>
      <g role="img" aria-label="Scales of justice and law books on a desk">
        <circle cx="561" cy="360" r="113" fill="url(#scales-photo)"/>
      </g>
      <circle cx="655" cy="442" r="80" fill="#ffffff"/>
      <circle cx="655" cy="442" r="72" fill="none" stroke="var(--gold)" stroke-width="5"/>
      <g role="img" aria-label="Open laptop computer">
        <circle cx="655" cy="442" r="66" fill="url(#laptop-photo)"/>
      </g>
    </g>

    <!-- Panel 3: cover -->
    <g class="panel-cover">
      <rect x="760" y="0" width="380" height="705" fill="url(#paper-fill)"/>
      <path d="M760 240C790 420 900 540 1140 510V705H760Z" fill="url(#gold-fill)"/>
      <path d="M790 250C840 180 920 160 1000 168C1070 176 1120 210 1140 240V280C1110 230 1060 196 990 192C920 188 860 210 818 262Z" fill="var(--gold)"/>
      <path d="M782 320C790 470 900 580 1045 558C960 552 860 500 812 340Z" fill="var(--charcoal)"/>
      <circle cx="956" cy="367" r="188" fill="#ffffff"/>
      <g role="img" aria-label="Attorney holding a leather folder with colleagues at a conference table">
        <circle cx="956" cy="367" r="176" fill="url(#team-photo)"/>
      </g>
      <circle cx="806" cy="272" r="12" fill="var(--gold)"/>
      <circle cx="794" cy="316" r="16" fill="var(--charcoal)"/>
      <rect x="760" y="687" width="380" height="18" fill="var(--charcoal)"/>
    </g>
  </svg>

  <section class="why-text">
    <h3>Why should every parent have a will?</h3>
    <p>Imagine how many people love your children. Would there be a fight over who would care for your children if you passed away without leaving instructions?</p>
    <p>Naming a guardian in your will helps avoid litigation that would cause additional stress to your children and loved ones. You can also name a back-up in the event that your first choice is unable or unwilling to serve as guardian.</p>
    <h3>What does the estate planning package include?</h3>
    <p>Our estate planning package includes a will, an advance medical directive, and a power of attorney. A will names a guardian for your children and gives instructions on how to distribute your probate property at death. An advance medical directive, also known as a living will, states directions regarding your healthcare decisions in the event that you can't make those decisions yourself. A power of attorney gives someone the ability to handle your financial affairs during your lifetime.</p>
  </section>

  <section class="offer">
    <div class="offer-price">
      <div class="amount">$750</div>
      <div class="per">PER COUPLE</div>
    </div>
    <div class="offer-terms">For parents-to-be and<br>parents of children<br>under 5 years old.</div>
  </section>

  <section class="contact">
    <h2>CONTACT US</h2>
    <p>418 E. Linden Avenue,</p>
    <p>Suite 310, Fairmont, MD 21290</p>
    <p>P: (410)-555-0148 &nbsp;F: (410)-555-0163</p>
    <p>E: claire@hartwell-legal.com</p>
    <p>www.hartwell-legal.com</p>
  </section>

  <header class="brand">
    <span class="brand-dot"></span>
    <span class="brand-name">HARTWELL<br>LEGAL, LLC</span>
  </header>

  <h1 class="cover-headline">
    <span class="lead">Estate Planning Special</span>
    <span class="accent">For New Parents</span>
  </h1>
</main>
</body>
</html>
```